Dovekin BTFM Leadership Academy

Would like a flyer designed for this program. Playing off of the "Take Wing" tag line. The BTFM is acronym for "build trust, foster momentum". It is a leadership/people development program aimed at training human (aka "conscious") leadership skills. Maybe play around with B T F M stacked (can't get the superscript to work here). Website is www.dovekin.com. Would like the same color palette. Want a high energy, power vibe. Want a light background on the flyer.
The presentation is intended to inform the content included in the flyer. Would like succinct messaging with clean, clear aesthetic. Include high-level overview of the program details included in the ppt slides.

Target Market(s)

Organizations looking for leadership development programs

Font styles to use
Serif

Requirements
Must have
• include call to action with contact info - qr code to dovekin.com, email mave@dovekin.com

```html
<!DOCTYPE html>
<html lang="en">
<head>
<meta charset="UTF-8">
<title>Dovekin BTFM Leadership Program Brochure</title>
<link href="https://fonts.googleapis.com/css2?family=Cinzel:wght@600;700&family=Lora:wght@400;600&display=swap" rel="stylesheet">
<style>
  :root{
    --bg:#e6e7e8;
    --paper:#ffffff;
    --green:#6aa62c;
    --lime:#9ccc3c;
    --deep-green:#3f7d1f;
    --navy:#1d2b4b;
    --brown:#6b4a2b;
    --ink:#4a4a4a;
    --muted:#8a8a8a;
    --pale:#eef5e4;
  }
  *{box-sizing:border-box;margin:0;padding:0}
  html,body{width:1200px;height:2700px;overflow:hidden;background:var(--bg)}
  body{font-family:'Lora',Georgia,serif;color:var(--ink);display:flex;flex-direction:column;align-items:center;gap:70px;padding-top:50px}
  .heading{font-family:'Cinzel',Georgia,serif;font-weight:700;color:var(--deep-green);letter-spacing:1px}
  .page{position:relative;background:var(--paper);overflow:hidden}
  .spread{display:flex;width:1100px;height:600px;box-shadow:0 6px 18px rgba(0,0,0,.18)}
  .spread .page{width:550px;height:600px}
  .spread .page:first-child{border-right:1px solid #ddd}
  .photo{position:absolute}
  .bg-svg{position:absolute;inset:0;width:100%;height:100%}

  /* Cover */
  .cover{width:700px;height:540px;box-shadow:0 6px 18px rgba(0,0,0,.18)}
  .cover .photo{left:6%;top:10%;width:38%;height:80%;background:radial-gradient(ellipse at 50% 60%,#dfe9d2 0%,#f4f7ef 55%,#fff 100%)}
  .cover-url{position:absolute;left:2%;top:50%;transform:translate(-38%,-50%) rotate(-90deg);font-size:12px;letter-spacing:2px;color:var(--muted)}
  .cover-title{position:absolute;left:55%;top:11%;width:41%;font-family:'Cinzel',Georgia,serif;font-weight:700;color:#fff;font-size:34px;line-height:1.15;letter-spacing:1px}
  .cover-sub{position:absolute;left:55%;top:46%;width:40%;color:#fff;font-size:17px;line-height:1.35}
  .brand{position:absolute;display:flex;align-items:center;gap:10px;font-family:'Cinzel',Georgia,serif;font-weight:700;color:#fff;font-size:22px;letter-spacing:2px}
  .brand .dot{width:26px;height:26px;border-radius:50%;background:#fff;opacity:.9}
  .cover .brand{left:62%;bottom:9%}
  .spread .cover{width:550px;height:600px;box-shadow:none}
  .spread .cover .cover-title{font-size:28px}
  .spread .cover .cover-sub{font-size:15px}
  .spread .cover .brand{font-size:18px}

  /* Program intro */
  .intro-title{position:absolute;left:40px;top:40px;font-size:32px}
  .intro .sub{position:absolute;left:40px;top:92px;font-family:'Cinzel',Georgia,serif;font-size:13px;color:var(--navy);letter-spacing:1px}
  .intro .body{position:absolute;left:40px;top:120px;width:250px;font-size:13px;line-height:1.6}
  .intro .body p+p{margin-top:10px}
  .halo{position:absolute;left:300px;top:130px;width:220px;height:220px;border-radius:50%;background:radial-gradient(circle,#fffbe0 0%,#f3f8c8 45%,rgba(255,255,255,0) 72%)}
  .halo-mark{position:absolute;left:50%;top:50%;transform:translate(-50%,-50%);width:96px;height:96px;border-radius:50%;border:3px solid var(--green);background:#fff}
  .intro .brand{left:330px;top:370px;color:var(--deep-green);font-size:22px}
  .intro .brand .dot{background:var(--green)}
  .contact{position:absolute;left:40px;top:330px;display:flex;align-items:center;gap:14px}
  .qr{width:84px;height:84px;background:var(--navy);border:6px solid #fff;outline:2px solid var(--navy)}
  .contact-text{font-size:13px;line-height:1.6;color:var(--navy)}
  .contact-text strong{font-family:'Cinzel',Georgia,serif;font-weight:700;color:var(--deep-green);font-size:14px;display:block}

  /* Objective */
  .objective .photo{left:0;top:60px;width:150px;height:300px;background:linear-gradient(135deg,#c9452f,#e59b2d 30%,#3b3b3b 60%,#8a8a8a)}
  .objective-title{position:absolute;left:170px;top:56px;font-size:30px}
  .bullets{list-style:none;font-size:13px;line-height:1.7}
  .bullets li::before{content:"";display:inline-block;width:7px;height:7px;border-radius:50%;background:var(--green);margin-right:8px;vertical-align:middle}
  .objective .bullets{position:absolute;left:172px;top:104px}
  .diagram{position:absolute}
  .diagram text{font-family:'Lora',Georgia,serif;font-size:12px;fill:var(--navy);text-anchor:middle}
  .diagram .core{font-family:'Cinzel',Georgia,serif;font-weight:700;font-size:15px;fill:#fff}

  /* Who is it for */
  .who .photo{right:0;top:0;width:300px;height:210px;background:linear-gradient(160deg,#f1f1f1,#c9cdd2 60%,#8c949e)}
  .who-title{position:absolute;left:34px;top:36px;width:220px;font-size:26px;line-height:1.2}
  .who .bullets{position:absolute;left:36px;top:110px}
  .who .band{position:absolute;left:0;top:250px;width:100%;height:8px;background:var(--navy)}
  .modules-title{position:absolute;left:190px;top:285px;font-size:18px;color:var(--navy)}
  .doc{position:absolute;top:330px;width:150px;height:190px;background:#fff;border:1px solid #cfd3d8;box-shadow:4px 4px 0 #e3e6ea}
  .doc h4{font-family:'Cinzel',Georgia,serif;font-size:12px;color:#fff;background:var(--green);padding:8px;line-height:1.3}
  .doc .line{height:6px;margin:12px 12px 0;background:#e2e6de;border-radius:3px}

  /* Individual / Teams / Organization */
  .individual .photo{left:0;top:0;width:230px;height:600px;background:linear-gradient(180deg,#9ec6d6,#c7dde6 50%,#d9b98e 80%,#a97f4f)}
  .individual-title{position:absolute;left:250px;top:260px;font-size:28px;color:var(--navy)}
  .individual .note{position:absolute;left:252px;top:298px;font-size:13px;color:var(--muted)}
  .teams .photo{left:0;top:0;width:260px;height:200px;background:linear-gradient(135deg,#e8e2d8,#b7a48e 55%,#6f6356)}
  .teams-title{position:absolute;left:280px;top:24px;font-size:24px;color:var(--navy)}
  .section-note{display:block;font-family:'Lora',Georgia,serif;font-weight:400;font-size:12px;color:var(--muted);letter-spacing:0;margin-top:2px}
  .boxes{position:absolute;left:280px;top:86px;display:flex;flex-direction:column;gap:8px}
  .boxes div{width:240px;padding:10px 12px;color:#fff;font-size:13px}
  .boxes .b1{background:var(--navy)} .boxes .b2{background:var(--green)} .boxes .b3{background:var(--brown)}
  .org-title{position:absolute;left:250px;top:260px;font-size:24px;color:var(--navy)}
  .swoosh{position:absolute;left:0;bottom:0;width:100%;height:90px}
</style>
</head>
<body>

<section class="page cover">
  <svg class="bg-svg" viewBox="0 0 700 540" preserveAspectRatio="none" aria-hidden="true">
    <defs>
      <linearGradient id="coverGreen" x1="0" y1="0" x2="1" y2="1">
        <stop offset="0" stop-color="#9ccc3c"/><stop offset="1" stop-color="#3f7d1f"/>
      </linearGradient>
    </defs>
    <path d="M345 0 Q285 270 345 540 L700 540 L700 0 Z" fill="url(#coverGreen)"/>
    <path d="M325 0 Q265 270 325 540" fill="none" stroke="#1d2b4b" stroke-width="14"/>
  </svg>
  <div class="photo" role="img" aria-label="Delicate branching twig with small white buds on a light background"></div>
  <div class="cover-url">www.dovekin.com</div>
  <h1 class="cover-title">Build Trust, Foster Momentum</h1>
  <p class="cover-sub">Dovekin BTFM Leadership Program</p>
  <div class="brand"><span class="dot"></span>Dovekin</div>
</section>

<section class="spread">
  <article class="page intro">
    <h2 class="heading intro-title">BTFM Program</h2>
    <p class="sub">Concept and Purpose</p>
    <div class="body">
      <p>A guided journey that grows conscious leaders who build trust, lift teams and drive lasting results across the whole organization.</p>
      <p>Eight months of workshops, coaching and peer circles turn insight into daily action.</p>
    </div>
    <div class="halo"><span class="halo-mark"></span></div>
    <div class="contact">
      <div class="qr" role="img" aria-label="QR code linking to dovekin.com"></div>
      <p class="contact-text"><strong>Take Wing</strong>Scan to visit dovekin.com<br>mave@dovekin.com</p>
    </div>
    <div class="brand"><span class="dot"></span>Dovekin</div>
    <svg class="swoosh" viewBox="0 0 550 90" preserveAspectRatio="none" aria-hidden="true">
      <path d="M0 60 Q275 10 550 40 L550 90 L0 90 Z" fill="#9ccc3c"/>
      <path d="M0 75 Q275 30 550 60 L550 90 L0 90 Z" fill="#6aa62c"/>
    </svg>
  </article>
  <article class="page cover">
    <svg class="bg-svg" viewBox="0 0 700 540" preserveAspectRatio="none" aria-hidden="true">
      <path d="M345 0 Q285 270 345 540 L700 540 L700 0 Z" fill="url(#coverGreen)"/>
      <path d="M325 0 Q265 270 325 540" fill="none" stroke="#1d2b4b" stroke-width="14"/>
    </svg>
    <div class="photo" role="img" aria-label="Delicate branching twig with small white buds on a light background"></div>
    <h2 class="cover-title">Build Trust, Foster Momentum</h2>
    <p class="cover-sub">Dovekin BTFM Leadership Program</p>
    <div class="brand"><span class="dot"></span>Dovekin</div>
  </article>
</section>

<section class="spread">
  <article class="page objective">
    <div class="photo" role="img" aria-label="Fan of coloured pencils with one red pencil standing out"></div>
    <h2 class="heading objective-title">The Objective</h2>
    <ul class="bullets">
      <li>Grow self-aware, human leaders</li>
      <li>Strengthen trust within teams</li>
      <li>Align people with purpose</li>
    </ul>
    <svg class="diagram" style="left:150px;top:210px" width="390" height="330" viewBox="0 0 390 330">
      <g stroke="#1d2b4b" stroke-width="2">
        <line x1="195" y1="165" x2="80" y2="70"/><line x1="195" y1="165" x2="310" y2="70"/>
        <line x1="195" y1="165" x2="80" y2="260"/><line x1="195" y1="165" x2="310" y2="260"/>
      </g>
      <g fill="#fff" stroke-width="5">
        <circle cx="80" cy="70" r="44" stroke="#1d2b4b"/><circle cx="310" cy="70" r="44" stroke="#6aa62c"/>
        <circle cx="80" cy="260" r="44" stroke="#6aa62c"/><circle cx="310" cy="260" r="44" stroke="#1d2b4b"/>
      </g>
      <circle cx="195" cy="165" r="50" fill="#6aa62c" stroke="#1d2b4b" stroke-width="5"/>
      <text x="195" y="170" class="core">BTFM</text>
      <text x="80" y="74">Self</text><text x="310" y="74">Team</text>
      <text x="80" y="264">Culture</text><text x="310" y="264">Results</text>
    </svg>
  </article>
  <article class="page who">
    <div class="photo" role="img" aria-label="Group of professionals leaping together against a bright sky"></div>
    <h2 class="heading who-title">Who is BTFM for:</h2>
    <ul class="bullets">
      <li>Emerging leaders</li><li>Senior managers</li><li>Executive teams</li><li>HR partners</li>
    </ul>
    <div class="band"></div>
    <h3 class="heading modules-title">BTFM Program Modules</h3>
    <div class="doc" style="left:190px"><h4>Module One: Inner Leader</h4><div class="line"></div><div class="line"></div><div class="line"></div><div class="line"></div></div>
    <div class="doc" style="left:360px"><h4>Module Two: Leading Others</h4><div class="line"></div><div class="line"></div><div class="line"></div><div class="line"></div></div>
  </article>
</section>

<section class="spread">
  <article class="page individual">
    <div class="photo" role="img" aria-label="Wooden blocks rising like steps against a pale blue sky"></div>
    <h2 class="heading individual-title">Individual</h2>
    <p class="note">(change in self)</p>
    <svg class="diagram" style="left:250px;top:330px" width="290" height="250" viewBox="0 0 290 250">
      <g fill="#fff" stroke-width="5">
        <circle cx="70" cy="60" r="48" stroke="#1d2b4b"/><circle cx="210" cy="60" r="48" stroke="#6aa62c"/>
        <circle cx="70" cy="190" r="48" stroke="#6aa62c"/><circle cx="210" cy="190" r="48" stroke="#1d2b4b"/>
      </g>
      <text x="70" y="64">Clarity</text><text x="210" y="64">Presence</text>
      <text x="70" y="194">Courage</text><text x="210" y="194">Growth</text>
    </svg>
  </article>
  <article class="page teams">
    <div class="photo" role="img" aria-label="Colleagues collaborating around a table in a bright office"></div>
    <h2 class="heading teams-title">Teams<span class="section-note">(change in how we work)</span></h2>
    <div class="boxes"><div class="b1">Connect</div><div class="b2">Collaborate</div><div class="b3">Commit</div></div>
    <h2 class="heading org-title">Organization<span class="section-note">(change in results)</span></h2>
    <svg class="diagram" style="left:40px;top:360px" width="480" height="200" viewBox="0 0 480 200">
      <g stroke="#1d2b4b" stroke-width="2"><line x1="90" y1="100" x2="390" y2="100"/></g>
      <g fill="#fff" stroke-width="5">
        <circle cx="90" cy="100" r="56" stroke="#6aa62c"/><circle cx="240" cy="100" r="56" stroke="#1d2b4b"/><circle cx="390" cy="100" r="56" stroke="#6aa62c"/>
      </g>
      <text x="90" y="104">Culture</text><text x="240" y="104">Engagement</text><text x="390" y="104">Impact</text>
    </svg>
  </article>
</section>

</body>
</html>
```